Summit Relay Business Card

Side 1: Summit Relay Logo (logo without Maltese cross) with industrial rope rescue related theme. Our company services - TRAINING - Fire Training, Confined Space Rescue Training, Rope Rescue training, Hazmat Training, Incident Command, EMS, Pump Operations Training. Website - summitrelay-example.com.
Side 2: Summit Relay Fire Department Logo (logo with Maltese cross) with Firefighter related theme. Company (division) services - FIELD SERVICES - Fire Department, Stand-by Rescue, Safety, EMS, Planning. "Supporting the Emergency Response Community Since 1967"

Add contact information wherever it makes since (Name, Email, Phone).
I would like it to represent the Summit Relay Fire Department Logo as a division not as a separate entity without saying it, possibly by depicting it in the background of Side 2 instead of being a standalone picture like the logo on Side 1.

```html
<!DOCTYPE html>
<html lang="en">
<head>
<meta charset="utf-8">
<title>Summit Relay Business Card</title>
<link href="https://fonts.googleapis.com/css2?family=Poppins:wght@400;500;600;700&display=swap" rel="stylesheet">
<style>
  :root {
    --stage: #ececec;
    --signal-red: #ec0000;
    --paper: #ffffff;
    --ink: #1f1f1f;
    --ink-soft: #2b2b2b;
    --white: #ffffff;
  }
  * { box-sizing: border-box; margin: 0; padding: 0; }
  html, body { width: 1200px; height: 1108px; overflow: hidden; }
  body {
    background: var(--stage);
    font-family: "Poppins", sans-serif;
    position: relative;
  }
  .card {
    position: absolute;
    top: 200px;
    width: 420px;
    height: 700px;
    border-radius: 26px;
    box-shadow: 0 14px 34px rgba(0,0,0,0.18);
    overflow: hidden;
    text-align: center;
  }
  /* Side 2 — field services division */
  .card--field {
    left: 150px;
    background: var(--signal-red);
    color: var(--white);
  }
  .emblem-pattern {
    position: absolute;
    inset: 0;
    background: radial-gradient(circle at 50% 45%, #f20a0a 0%, var(--signal-red) 70%);
  }
  .field-content {
    position: relative;
    padding-top: 92px;
  }
  .section-title {
    font-weight: 600;
    font-size: 38px;
    letter-spacing: 0.5px;
    line-height: 1.1;
  }
  .service-list {
    list-style: none;
    margin-top: 16px;
    font-weight: 400;
    font-size: 22px;
    line-height: 1.28;
    text-transform: uppercase;
  }
  .rule-short {
    width: 44px;
    height: 1.5px;
    background: var(--white);
    margin: 26px auto;
  }
  .contact-name {
    font-weight: 600;
    font-size: 34px;
    line-height: 1.1;
  }
  .contact-lines {
    margin-top: 14px;
    font-size: 20px;
    line-height: 1.35;
  }
  .tagline {
    font-size: 17px;
    line-height: 1.4;
    font-weight: 500;
  }

  /* Side 1 — training */
  .card--training {
    left: 630px;
    background: var(--paper);
    color: var(--ink);
  }
  .brand {
    margin-top: 150px;
    display: flex;
    align-items: center;
    justify-content: center;
    gap: 12px;
  }
  .brand-mark {
    width: 18px;
    height: 18px;
    background: var(--signal-red);
  }
  .brand-name {
    font-weight: 700;
    font-size: 40px;
    color: var(--signal-red);
    text-transform: uppercase;
    letter-spacing: 1px;
  }
  .brand-rule {
    width: 300px;
    height: 3px;
    background: var(--signal-red);
    margin: 14px auto 0;
  }
  .card--training .section-title {
    margin-top: 70px;
    color: var(--signal-red);
    font-size: 40px;
  }
  .card--training .service-list {
    margin-top: 10px;
    font-size: 19px;
    line-height: 1.3;
    color: var(--ink-soft);
  }
  .rule-long {
    width: 330px;
    height: 1.5px;
    background: var(--signal-red);
    margin: 34px auto 22px;
  }
  .website {
    font-size: 20px;
    letter-spacing: 1.5px;
    color: var(--ink);
  }
  .website .web-name { color: var(--signal-red); }
</style>
</head>
<body>
  <section class="card card--field">
    <div class="emblem-pattern" role="img" aria-label="Faint repeated division emblem pattern across the red background"></div>
    <div class="field-content">
      <h2 class="section-title">FIELD SERVICES</h2>
      <ul class="service-list">
        <li>Fire Department</li>
        <li>Stand-by Rescue</li>
        <li>Safety</li>
        <li>EMS</li>
        <li>Planning</li>
      </ul>
      <div class="rule-short"></div>
      <p class="contact-name">Dana Whitfield</p>
      <p class="contact-lines">044-555 010 248<br>hello@summitrelay-example.com</p>
      <div class="rule-short"></div>
      <p class="tagline">Supporting the Emergency Response<br>Community Since 1967</p>
    </div>
  </section>

  <section class="card card--training">
    <div class="brand">
      <span class="brand-mark"></span>
      <span class="brand-name">Summit Relay</span>
    </div>
    <div class="brand-rule"></div>
    <h2 class="section-title">TRAINING</h2>
    <ul class="service-list">
      <li>Fire Training</li>
      <li>Confined Space Rescue Training</li>
      <li>Rope Rescue Training</li>
      <li>Hazmat Training</li>
      <li>Incident Command</li>
      <li>EMS</li>
      <li>Pump Operations Training</li>
    </ul>
    <div class="rule-long"></div>
    <p class="website">www.<span class="web-name">summitrelay-example</span>.com</p>
  </section>
</body>
</html>
```